Business Card Design

Quiet Meadows - edgy, unique, ontrend clothing for girls 0-12.
I would like simple styling with white background and natural beige/brown font, similar to attached font.

Industry/Entity Type

Clothing

Contact Information for Business Card

Hi, I would like a very simple business card, white background with natural, beige, brown font, Quiet Meadows. I design and sell clothes for girls 0-12 with a touch of bohemian styling. I would like "Quiet Meadows" on front and on back -
www.quietmeadows-example.com.au
Delia Hartwell,
0481552937,
deliahartwell@brightnest-mail.com.au

```html
<!DOCTYPE html>
<html lang="en">
<head>
<meta charset="utf-8">
<title>Quiet Meadows – Business Card</title>
<link rel="stylesheet" href="https://fonts.googleapis.com/css2?family=Gochi+Hand&display=swap">
<style>
  :root {
    --page-bg: #f1f0ec;
    --card-white: #ffffff;
    --olive: #85805f;
    --olive-text: #7d7657;
    --orange: #d8924c;
    --url-orange: #d9893a;
    --ink-light: #ffffff;
    --card-shadow: 0 6px 18px rgba(0, 0, 0, 0.18);
  }
  * { box-sizing: border-box; margin: 0; padding: 0; }
  html, body {
    width: 1200px;
    height: 741px;
    overflow: hidden;
    background: var(--page-bg);
  }
  .canvas {
    position: relative;
    width: 1200px;
    height: 741px;
    font-family: "Gochi Hand", cursive;
  }
  .card {
    position: absolute;
    width: 540px;
    height: 310px;
    box-shadow: var(--card-shadow);
    overflow: hidden;
  }

  /* Front */
  .card--front {
    left: 50px;
    top: 60px;
    background: var(--card-white);
  }
  .card--front .brand-name {
    position: absolute;
    top: 78px;
    width: 100%;
    text-align: center;
    font-size: 50px;
    line-height: 1;
    color: var(--olive-text);
  }
  .card--front .web-address {
    position: absolute;
    top: 140px;
    width: 100%;
    text-align: center;
    font-size: 18px;
    color: var(--url-orange);
  }
  .contact-band {
    position: absolute;
    left: 0;
    bottom: 0;
    width: 100%;
    height: 78px;
    background: var(--orange);
  }
  .holder-name {
    position: absolute;
    left: 22px;
    bottom: 82px;
    font-size: 27px;
    line-height: 1;
    color: var(--olive-text);
  }
  .contact-lines {
    position: absolute;
    left: 22px;
    bottom: 14px;
    list-style: none;
    font-size: 16px;
    line-height: 1.35;
    color: var(--ink-light);
  }

  /* Back */
  .card--back {
    left: 610px;
    top: 370px;
    background: var(--olive);
  }
  .card--back .brand-name {
    position: absolute;
    right: 34px;
    bottom: 78px;
    font-size: 62px;
    line-height: 1;
    color: var(--ink-light);
  }
  .card--back .web-address {
    position: absolute;
    right: 34px;
    bottom: 44px;
    font-size: 22px;
    color: var(--ink-light);
  }
</style>
</head>
<body>
  <main class="canvas">
    <section class="card card--front" aria-label="Business card front">
      <h1 class="brand-name">Quiet Meadows</h1>
      <p class="web-address">www.quietmeadows-example.com.au</p>
      <div class="contact-band"></div>
      <p class="holder-name">Delia Hartwell</p>
      <ul class="contact-lines">
        <li>T: 0481552937</li>
        <li>E: deliahartwell@brightnest-mail.com.au</li>
      </ul>
    </section>

    <section class="card card--back" aria-label="Business card back">
      <h2 class="brand-name">Quiet Meadows</h2>
      <p class="web-address">www.quietmeadows-example.com.au</p>
    </section>
  </main>
</body>
</html>
```